Refresh our Logo and Letterhead!

We would like to see designs with blue, green, teal etc. Our current logo and contact details for the letterhead is attached.
We're a small boutique firm based in Sydney, Australia. We're near the coast and not opposed to coastal images. We practice in property law and have primarily female practitioners, although we don't necessarily need the logo and letterhead to be too feminine. We would like to see designs with blue, green, teal etc. Our current logo and contact details for the letterhead is attached.
We're a small boutique firm based in Sydney, Australia. We're near the coast and not opposed to coastal images. We practice in property law and have primarily female practitioners, although we don't necessarily need the logo and letterhead to be too feminine.

Target Market(s)

Young professionals

Industry/Entity Type

Law Firm

Logo Text

Marwick Legal

Font styles to use
Serif
Sans Serif

Colors
34a7d8
00a990
85acd3
886aae

Requirements
Must have
• The letterhead must have the text in the "contact info" jpg uploaded with the brief.
Nice to have
• We'd like to see some simple, innovating, fresh ideas. A watermark or something interesting in the background would be good.

```html
<!DOCTYPE html>
<html lang="en">
<head>
<meta charset="utf-8">
<title>Marwick Legal Letterhead</title>
<link href="https://fonts.googleapis.com/css2?family=Open+Sans:wght@400&family=Roboto:wght@400&display=swap" rel="stylesheet">
<style>
  :root {
    --backdrop: #e4e4e4;
    --paper: #f6f6f6;
    --brand-blue: #2f6fb1;
    --brand-sky: #4fb3e3;
    --body-text: #676767;
    --footer-text: #555555;
    --signature-tone: #dcdcdc;
  }
  * { box-sizing: border-box; margin: 0; padding: 0; }
  html, body {
    width: 1097px; height: 1200px; overflow: hidden;
    background: var(--backdrop);
  }
  .letterhead {
    position: absolute;
    left: 146px; top: 30px;
    width: 805px; height: 1140px;
    background: var(--paper);
    box-shadow: 0 6px 18px rgba(0,0,0,0.18);
    font-family: "Open Sans", sans-serif;
    color: var(--body-text);
  }
  .brand {
    position: absolute; left: 58px; top: 100px;
    display: flex; align-items: center; gap: 14px;
  }
  .brand-mark {
    width: 26px; height: 26px; border-radius: 50%;
    background: var(--brand-sky);
  }
  .brand-name {
    font-family: "Open Sans", sans-serif;
    font-size: 46px; font-weight: 400;
    color: var(--brand-blue); letter-spacing: 0.5px;
  }
  .letter-body {
    position: absolute; left: 58px; top: 219px; width: 689px;
    font-size: 15.6px; line-height: 23px;
  }
  .greeting { margin-bottom: 23px; }
  .letter-body p.paragraph { text-align: justify; margin-bottom: 23px; }
  .sign-off { margin-top: 0; }
  .signature {
    position: absolute; left: 58px; top: 823px;
    width: 100px; height: 96px; background: var(--signature-tone);
    border-radius: 4px;
  }
  .contact-list {
    position: absolute; left: 58px; top: 954px;
    list-style: none;
    font-family: "Roboto", sans-serif; font-size: 15.5px; line-height: 21px;
    color: var(--footer-text);
  }
  .contact-list li { display: flex; align-items: center; gap: 5px; }
  .contact-list svg { width: 13px; height: 13px; fill: var(--brand-blue); flex: none; }
  .postal { padding-left: 2px; }
  .firm-details {
    position: absolute; right: 58px; top: 959px; text-align: right;
    font-family: "Roboto", sans-serif; font-size: 15.5px; line-height: 19.5px;
    color: var(--footer-text);
  }
  .firm-details .firm-name, .firm-details .abn-label { color: var(--brand-blue); }
  .firm-details .firm-name, .firm-details .abn { margin-bottom: 2px; }
  .firm-details .abn { margin-bottom: 4px; }
</style>
</head>
<body>
  <main class="letterhead">
    <header class="brand">
      <span class="brand-mark"></span>
      <span class="brand-name">Marwick Legal</span>
    </header>

    <section class="letter-body">
      <p class="greeting">Dear customer,</p>
      <p class="paragraph">Lorem ipsum dolor sit amet, consectetur adipisicing elit, sed do eiusmod tempor incididunt ut labore et dolore magna aliqua. Ut enim ad minim veniam, quis nostrud exercitation ullamco laboris nisi ut aliquip ex ea commodo consequat. Duis aute irure dolor in reprehenderit in voluptate velit esse cillum dolore eu fugiat nulla pariatur. Excepteur sint occaecat cupidatat non proident, sunt in culpa qui officia deserunt mollit anim id est laborum.</p>
      <p class="paragraph">Lorem ipsum dolor sit amet, consectetur adipisicing elit, sed do eiusmod tempor incididunt ut labore et dolore magna aliqua. Ut enim ad minim veniam, quis nostrud exercitation ullamco laboris nisi ut aliquip ex ea commodo consequat. Duis aute irure dolor in reprehenderit in voluptate velit esse cillum dolore eu fugiat nulla pariatur. Excepteur sint occaecat cupidatat non proident, sunt in culpa qui officia deserunt mollit anim id est laborum.</p>
      <p class="paragraph">Lorem ipsum dolor sit amet, consectetur adipisicing elit, sed do eiusmod tempor incididunt ut labore et dolore magna aliqua. Ut enim ad minim veniam, quis nostrud exercitation ullamco laboris nisi ut aliquip ex ea commodo consequat. Duis aute irure dolor in reprehenderit in voluptate velit esse cillum dolore eu fugiat nulla pariatur. Excepteur sint occaecat cupidatat non proident, sunt in culpa qui officia deserunt mollit anim id est laborum.</p>
      <p class="paragraph">Lorem ipsum dolor sit amet, consectetur adipisicing elit, sed do eiusmod tempor incididunt ut labore et dolore magna aliqua. Ut enim ad minim veniam, quis nostrud exercitation ullamco laboris nisi ut aliquip ex ea commodo consequat. Duis aute irure dolor in reprehenderit.</p>
      <p class="sign-off">Yours Sincerely,</p>
    </section>

    <div class="signature" role="img" aria-label="Handwritten signature of the sender"></div>

    <ul class="contact-list">
      <li class="postal">P O Box 412, Avoca Beach NSW 2251</li>
      <li><svg viewBox="0 0 16 16"><path d="M4 0h8a1 1 0 0 1 1 1v14a1 1 0 0 1-1 1H4a1 1 0 0 1-1-1V1a1 1 0 0 1 1-1zm1 2v10h6V2zm3 11a1 1 0 1 0 0 2 1 1 0 0 0 0-2z"/></svg>0431 058 216</li>
      <li><svg viewBox="0 0 16 16"><path d="M1 6c1-3 13-3 14 0l-1 2-3-1V5H5v2L2 8zM4 9h8l2 5H2z"/></svg>02 4382 1176</li>
      <li><svg viewBox="0 0 16 16"><path d="M4 1h8v4H4zM1 6h14v6h-3v3H4v-3H1zm4 4v4h6v-4z"/></svg>02 8214 6093</li>
      <li><svg viewBox="0 0 16 16"><path d="M0 3h16v10H0zm1.5 1L8 9l6.5-5z"/></svg>Sarah@marwicklegal.com.au</li>
      <li><svg viewBox="0 0 16 16"><path d="M8 0a5.5 5.5 0 0 1 5.5 5.5C13.5 10 8 16 8 16S2.5 10 2.5 5.5A5.5 5.5 0 0 1 8 0zm0 3.5a2 2 0 1 0 0 4 2 2 0 0 0 0-4z"/></svg>18 Bayview Crescent Avoca Beach NSW 2251</li>
    </ul>

    <aside class="firm-details">
      <p class="firm-name">Marwick Legal Pty Ltd</p>
      <p class="abn"><span class="abn-label">ABN :</span> 51 602 384 917</p>
      <p>An incorporated legal practice under the<br>Legal Profession Act 2004 as amended.</p>
      <p>Liability Limited by a scheme approved under<br>Professional Standards Legislation</p>
    </aside>
  </main>
</body>
</html>
```